Postcard Design www.harborlineclaims.example

We need a new postcard design that would show our over 25 years of knowledge and expertise, yet touch on the functions and services we can perform, in Medical Billing. The problem is that the competition is fierce, with many many new Medical Billing Companies getting in the act. Unfortunately these companies can be extremely hurtful to the financial well being of medical providers, as they do not know the laws, regulations, nor have the expertise.
Updates

I just received my final approval on my trademark, so the phrase Where Patience Pays & Detail Delivers is now a registered trademark. Also I just realized on my original postcard there is a typo. It should read Over 25 years in claims, billing, and revenue recovery, the "the" should not be there. Also I would like the "free 10 chart/EOB audit" to be a bigger deal that would catch the readers eye, maybe an expiration date or some other "call to action"

Target Market(s)

Target business is medical professionals. Chiropractors, Home Health providers, providers that would have large insurance clientele (Vitalcover, PPO).
NOT targeting Familiy Practice, Pediatricians, Hospitals, Dentists.

Industry/Entity Type

Financial

Font styles to use
Serif
Sans Serif

Colors
ec1f27
3277b5
ffffff

Requirements
Must have
• New ideas not just copied from my existing postcard. Something that somehow tells the story of going with inexperience can cost you.

```html
<!DOCTYPE html>
<html lang="en">
<head>
<meta charset="utf-8">
<title>Harborline Medical Claims &amp; Audit – Postcard</title>
<link rel="stylesheet" href="https://fonts.googleapis.com/css2?family=Libre+Baskerville:ital,wght@0,700;1,400&family=PT+Sans:ital,wght@0,400;0,700;1,700&display=swap">
<style>
  :root {
    --brand-blue: #3277b5;
    --brand-blue-dark: #245d92;
    --brand-red: #ec1f27;
    --paper: #ffffff;
    --ink: #1a1a1a;
    --url-yellow: #f4e23a;
    --seal-gold: #f3a52a;
    --backdrop: #e9e9ec;
    --rule-blue: #2a5ea6;
  }
  * { box-sizing: border-box; margin: 0; padding: 0; }
  html, body {
    width: 1200px; height: 750px; overflow: hidden;
    background: var(--backdrop);
  }
  .postcard {
    position: absolute; left: 176px; top: 47px;
    width: 848px; height: 656px;
    background: var(--paper);
    box-shadow: 0 6px 18px rgba(0,0,0,0.18);
    overflow: hidden;
  }
  .url-bar {
    position: absolute; left: 0; top: 0; width: 403px; height: 58px;
    background: var(--brand-blue);
    display: flex; align-items: center; justify-content: center;
    font-family: "PT Sans", sans-serif; font-weight: 700;
    font-size: 19px; letter-spacing: 1.2px; color: var(--url-yellow);
  }
  .brand-mark {
    position: absolute; left: 22px; top: 160px;
    display: flex; align-items: center; gap: 8px;
  }
  .brand-mark__dot {
    width: 22px; height: 22px; border-radius: 50%;
    background: var(--brand-red);
  }
  .brand-mark__name {
    font-family: "Libre Baskerville", serif; font-weight: 700;
    font-size: 23px; color: var(--brand-red);
  }
  .experience-seal {
    position: absolute; left: 240px; top: 118px;
    width: 138px; height: 138px; border-radius: 50%;
    background: var(--seal-gold);
  }
  .name-band { position: absolute; left: 0; top: 262px; }
  .name-band__title {
    position: absolute; left: 0; top: 292px; width: 403px;
    text-align: center; color: var(--paper);
    font-family: "Libre Baskerville", serif; font-weight: 700;
    font-size: 26px; line-height: 1.3; text-transform: uppercase;
  }
  .name-band__tagline {
    position: absolute; left: 0; top: 396px; width: 403px;
    text-align: center; color: var(--paper);
    font-family: "Libre Baskerville", serif; font-weight: 400; font-style: italic;
    font-size: 14px;
  }
  .address {
    position: absolute; left: 0; top: 440px; width: 403px;
    text-align: center; color: var(--ink);
    font-family: "PT Sans", sans-serif; font-style: italic; font-weight: 700;
    font-size: 23px; line-height: 1.2;
  }
  .contact-band {
    position: absolute; left: 0; top: 562px; width: 403px; height: 80px;
    background: var(--brand-blue);
    display: flex; flex-direction: column; justify-content: center; align-items: center;
    color: var(--paper);
    font-family: "PT Sans", sans-serif; font-style: italic; font-weight: 700;
    font-size: 20px; line-height: 1.3;
  }
  .story {
    position: absolute; left: 440px; top: 50px; width: 180px;
    font-family: "PT Sans", sans-serif; color: var(--ink);
  }
  .story__headline {
    font-family: "Libre Baskerville", serif; font-weight: 700;
    font-size: 19px; line-height: 1.25; color: var(--brand-red);
    margin-bottom: 10px;
  }
  .story__body { font-size: 14.5px; line-height: 1.35; }
  .story__body strong { color: var(--brand-blue); }
  .stamp-box {
    position: absolute; left: 646px; top: 46px; width: 141px; height: 142px;
    border: 2px solid var(--rule-blue);
  }
  .address-lines { position: absolute; left: 500px; top: 316px; width: 309px; }
  .address-lines span {
    display: block; height: 2px; background: var(--rule-blue); margin-bottom: 33px;
  }
  .audit-offer {
    position: absolute; left: 440px; top: 552px; width: 380px; height: 84px;
    background: var(--brand-red); color: var(--paper);
    display: flex; flex-direction: column; justify-content: center; align-items: center;
    font-family: "PT Sans", sans-serif; text-align: center;
  }
  .audit-offer__title { font-weight: 700; font-size: 23px; text-transform: uppercase; letter-spacing: 0.5px; }
  .audit-offer__note { font-size: 14.5px; }
</style>
</head>
<body>
  <main class="postcard">
    <header class="url-bar">www.harborlineclaims.example</header>

    <div class="brand-mark">
      <span class="brand-mark__dot"></span>
      <span class="brand-mark__name">Harborline</span>
    </div>

    <div class="experience-seal" aria-hidden="true"></div>

    <svg class="name-band" width="420" height="190" viewBox="0 0 420 190" aria-hidden="true">
      <polygon points="0,22 118,22 150,0 182,22 403,22 403,170 0,170" fill="var(--brand-blue)"/>
      <polygon points="0,118 403,118 403,170 0,170" fill="var(--brand-blue-dark)" opacity="0.35"/>
    </svg>
    <h1 class="name-band__title">Harborline Medical<br>Claims &amp; Audit</h1>
    <p class="name-band__tagline">Where Patience Pays &amp; Detail Delivers&reg;</p>

    <address class="address">
      4580 Juniper Row,<br># 210-337,<br>Alder Springs,<br>CA 90000
    </address>

    <footer class="contact-band">
      <span>Toll free(800) Harb-Line (555-0142)</span>
      <span>Fax (800) 555-0143</span>
    </footer>

    <section class="story">
      <h2 class="story__headline">Inexperience can cost you.</h2>
      <p class="story__body"><strong>Over 25 years</strong> in claims, billing, and revenue recovery for Vitalcover &amp; PPO providers.</p>
    </section>

    <div class="stamp-box"></div>
    <div class="address-lines">
      <span></span><span></span><span></span><span></span><span></span><span></span>
    </div>

    <aside class="audit-offer">
      <span class="audit-offer__title">Free 10 Chart/EOB Audit</span>
      <span class="audit-offer__note">Call today – offer expires December 31</span>
    </aside>
  </main>
</body>
</html>
```